Building Certification Company needs a professional letterhead and report template

We are a modern company within an ageing industry. Our industry is responsible for life safety aspects of the built environment, we ensure buildings are safe and fit for occupation.

We use letterhead and reports everyday, we need a smart and professional letterhead that reflects the serious nature of the work we do. We also require a report template of the same ilk.

Target Market(s)

Our target market will consist mainly of professional architects, developers and construction companies.

Industry/Entity Type

Industry

Requirements
Must have
• The letterhead must have:-
Our logo
Our company details, including address, website, email, phone

Address - Suite 208 / 45 Harwick Lane Dunmore NSW 2100

Website - www.quillstonecompliance.example.au

Email - info@qsc.example.au

Phone - 02 5550 3846

The report template must have:-
A title page, which is to incorporate our logo or an aspect of our logo, get creative people.

```html
<!DOCTYPE html>
<html lang="en">
<head>
<meta charset="utf-8">
<title>Quillstone Compliance Letterhead</title>
<link href="https://fonts.googleapis.com/css2?family=Tenor+Sans&display=swap" rel="stylesheet">
<style>
  :root {
    --paper: #ffffff;
    --navy: #1e3466;
    --ink: #2a3a5e;
    --accent: #2f5fc4;
    --rule: #7f95c8;
  }
  html, body {
    margin: 0;
    padding: 0;
    width: 861px;
    height: 1200px;
    overflow: hidden;
    background: var(--paper);
  }
  .letterhead {
    position: relative;
    width: 861px;
    height: 1200px;
    background: var(--paper);
    font-family: "Tenor Sans", "Optima", sans-serif;
    color: var(--ink);
  }
  .brand {
    position: absolute;
    left: 48px;
    top: 44px;
    width: 160px;
  }
  .brand-mark {
    width: 62px;
    height: 62px;
    background: var(--navy);
    margin: 0 0 18px 44px;
  }
  .brand-name {
    margin: 0;
    font-size: 17px;
    line-height: 1.3;
    letter-spacing: 1px;
    color: var(--navy);
    font-weight: 400;
    white-space: nowrap;
  }
  .divider {
    position: absolute;
    left: 222px;
    top: 124px;
    width: 1px;
    height: 56px;
    background: var(--rule);
  }
  .contact {
    position: absolute;
    left: 236px;
    top: 124px;
    margin: 0;
    font-size: 12px;
    line-height: 1.5;
    color: var(--ink);
    font-style: normal;
    white-space: nowrap;
  }
  .footer-rule {
    position: absolute;
    left: 58px;
    right: 64px;
    top: 1130px;
    height: 1px;
    background: var(--rule);
  }
  .footer-contact {
    position: absolute;
    left: 0;
    width: 861px;
    top: 1136px;
    margin: 0;
    text-align: center;
    font-size: 12px;
    color: var(--ink);
  }
  .corner-accent {
    position: absolute;
    right: 10px;
    bottom: 40px;
  }
</style>
</head>
<body>
  <main class="letterhead">
    <header class="brand">
      <div class="brand-mark"></div>
      <p class="brand-name">QUILLSTONE<br>COMPLIANCE</p>
    </header>
    <div class="divider"></div>
    <address class="contact">
      Suite 208 / 45 Harwick Lane,<br>
      Dunmore, NSW 2100<br>
      Phone: 02 5550 3846
    </address>

    <div class="footer-rule"></div>
    <p class="footer-contact">e: info@qsc.example.au &nbsp; w: www.quillstonecompliance.example.au</p>

    <svg class="corner-accent" width="110" height="56" viewBox="0 0 110 56" role="img" aria-label="Brand accent shape in blue">
      <polygon points="0,56 110,56 110,0" fill="var(--accent)"/>
    </svg>
  </main>
</body>
</html>
```